We need a web page design for a new company called "Quarry". We provide an innovative music sharing mobile application that allows music listeners to share their music without paying for a monthly subscription. We would like to incorporate the attached logo and color scheme. The final design should communicate music gifting and sharing.

Industry/Entity Type

It Company

```html
<!DOCTYPE html>
<html lang="en">
<head>
<meta charset="utf-8">
<title>Quarry – Share Music</title>
<link href="https://fonts.googleapis.com/css2?family=Source+Sans+Pro:wght@400;600;700&display=swap" rel="stylesheet">
<style>
:root{
  --green:#6bad19;
  --green-deep:#5a940f;
  --teal:#00bf90;
  --teal-shade:#0a9e73;
  --white:#ffffff;
  --input-border:#7ad321;
  --placeholder:#b7b7b7;
}
*{margin:0;padding:0;box-sizing:border-box}
html,body{width:1200px;height:1008px;overflow:hidden}
body{font-family:"Source Sans Pro",Arial,sans-serif;color:var(--white);position:relative;background:var(--green)}
.hero{position:absolute;left:0;top:0;width:1200px;height:489px;display:flex}
.hero-share{position:relative;width:599px;height:489px;
  background:linear-gradient(100deg,#1d2233 0%,#2a3045 28%,#8c8a86 48%,#b7b1a8 62%,#9aa2a6 100%)}
.hero-listen{width:601px;height:489px;
  background:linear-gradient(135deg,#5fd2b0 0%,#7be0c2 45%,#63cfae 75%,#4cbf9e 100%)}
.share-heading{position:absolute;right:46px;top:36px;text-align:right}
.share-heading h2{font-size:26px;font-weight:700;letter-spacing:.2px;line-height:1.1}
.share-heading p{font-size:15px;line-height:1.2;margin-top:1px}
.share-heading .rule{display:block;width:68px;height:2px;background:var(--white);margin:10px 0 0 auto;opacity:.85}
.subscribe{position:absolute;left:0;top:489px;width:1200px;height:474px;
  background:radial-gradient(ellipse 420px 400px at 600px 240px,#77b52a 0%,#6eae1f 55%,var(--green) 100%)}
.subscribe-body{position:absolute;left:0;right:0;top:102px;text-align:center}
.subscribe-body h1{font-size:26px;font-weight:400;letter-spacing:.3px;line-height:1.2}
.subscribe-body p{font-size:15px;margin-top:4px}
.subscribe-body .rule{display:block;width:68px;height:2px;background:rgba(255,255,255,.8);margin:12px auto 0}
.subscribe-form{position:absolute;left:443px;top:212px;width:366px}
.email-field{display:block;width:366px;height:55px;border:2px solid var(--input-border);border-radius:3px;
  background:linear-gradient(#ffffff,#f1f1f1);font:400 21px "Source Sans Pro",Arial,sans-serif;color:var(--placeholder);
  padding:0 16px;line-height:51px}
.subscribe-btn{display:block;width:366px;height:54px;margin-top:4px;border:0;border-radius:3px;
  background:var(--teal);box-shadow:0 3px 0 var(--teal-shade);color:var(--white);
  font:600 21px "Source Sans Pro",Arial,sans-serif;letter-spacing:.5px;line-height:54px;text-align:center}
.site-footer{position:absolute;left:0;top:963px;width:1200px;height:45px;background:var(--green-deep);
  display:flex;align-items:center;justify-content:space-between;padding:0 118px 0 112px}
.copyright{font-size:11.5px;display:flex;align-items:center;gap:6px}
.copyright .mark{font-size:15px}
.social-links{display:flex;gap:12px;align-items:center}
.social-links span{width:11px;height:11px;border-radius:50%;background:var(--white);opacity:.9}
</style>
</head>
<body>
<section class="hero">
  <div class="hero-share" role="img" aria-label="Photo of a person holding a smartphone with earphone cable">
    <div class="share-heading">
      <h2>SHARING IS CARING</h2>
      <p>Share with someone that matters to you</p>
      <span class="rule"></span>
    </div>
  </div>
  <div class="hero-listen" role="img" aria-label="Teal-tinted photo of a woman relaxing with headphones"></div>
</section>

<section class="subscribe" role="img" aria-label="Green-tinted background photo of a listener wearing headphones">
  <div class="subscribe-body">
    <h1>SUBSCRIBE FOR UPDATES</h1>
    <p>Subscripe for our newsletter and get the latest updates.</p>
    <span class="rule"></span>
  </div>
  <div class="subscribe-form">
    <div class="email-field">Email Address</div>
    <div class="subscribe-btn">SUBSCRIBE</div>
  </div>
</section>

<footer class="site-footer">
  <div class="copyright"><span class="mark">©</span>2014 Quarry - All Right Reserved</div>
  <nav class="social-links" aria-label="Social links">
    <span></span><span></span><span></span><span></span><span></span><span></span><span></span>
  </nav>
</footer>
</body>
</html>
```